KeyHarbor needs a modern business card

We are a modern conveyancing company and we need to appeal to the top (Multi-million dollar properties)and bottom on the property conveyancing market but our sweet spot is the middle of the market. I like professional with a hint of unconventional.

Target Market(s)

As above

Industry/Entity Type

Real Estate

Contact Information for Business Card

Back Of card:
thinking black with the logo and a tag line (I could be wrong about the black)
Tag line - Right Expertise, Exceptional Service

Front of Card:
Marissa Toll (BBus (Finance) LLB)
Licensed Conveyancer
Email: marissa@keyharbor.com.au

Key Harbor
ABN: 48 913 706
Suite 14, Level 3, 9 Calloway Road Lindhurst Park, NSW 2178
Phone: 1300 682 917

Sydney - Melbourne - Brisbane (Perhaps have this along the bottom of the card)

Requirements
Must have
• Sleek, modern and top end appeal (But approachable)
Should not have
• Not too cluttered

```html
<!DOCTYPE html>
<html lang="en">
<head>
<meta charset="utf-8">
<title>KeyHarbor Business Card</title>
<link href="https://fonts.googleapis.com/css2?family=Roboto:wght@400;500;700&display=swap" rel="stylesheet">
<style>
  :root {
    --backdrop: #a3a1a2;
    --card: #262626;
    --band: #395b82;
    --mark: #3a5f88;
    --white: #ffffff;
    --muted: #e2e2e2;
    --sky: #6db8ea;
    --accent-blue: #1e90ff;
    --accent-green: #7dc42b;
  }
  * { margin: 0; padding: 0; box-sizing: border-box; }
  html, body { width: 1200px; height: 1200px; overflow: hidden; }
  body {
    background: var(--backdrop);
    font-family: "Roboto", Arial, sans-serif;
    position: relative;
  }
  .card {
    position: absolute;
    left: 244px;
    width: 713px;
    height: 420px;
    background: var(--card);
    overflow: hidden;
  }
  .card--back { top: 117px; }
  .card--front { top: 642px; }

  .brand-square {
    position: absolute;
    width: 120px;
    height: 120px;
    background: var(--mark);
  }
  .brand-name {
    position: absolute;
    color: var(--white);
    font-weight: 500;
    font-size: 42px;
    letter-spacing: -0.5px;
    line-height: 1;
    text-align: center;
    width: 300px;
  }
  .card--back .brand-square { left: 297px; top: 95px; }
  .card--back .brand-name { left: 207px; top: 270px; }
  .card--front .brand-square { left: 129px; top: 100px; }
  .card--front .brand-name { left: 39px; top: 268px; }

  .band {
    position: absolute;
    left: 0; bottom: 0;
    width: 100%;
    height: 54px;
    background: var(--band);
    display: flex;
    align-items: center;
    justify-content: center;
    gap: 14px;
    color: var(--white);
    font-size: 18px;
    letter-spacing: 0.2px;
  }
  .band svg { display: block; }

  .details {
    position: absolute;
    left: 347px;
    top: 64px;
    color: var(--muted);
  }
  .person-name {
    color: var(--sky);
    font-weight: 700;
    font-size: 30px;
    line-height: 36px;
  }
  .credentials {
    font-size: 16.5px;
    line-height: 21px;
    margin-top: 4px;
  }
  .contact-list {
    list-style: none;
    margin-top: 23px;
    font-size: 18.5px;
    line-height: 26px;
  }
  .contact-list li { display: flex; align-items: center; gap: 16px; }
  .contact-list svg { width: 19px; height: 16px; flex: none; }
  .address {
    font-size: 18.5px;
    line-height: 26px;
    margin-top: 4px;
  }
</style>
</head>
<body>

<section class="card card--back">
  <div class="brand-square"></div>
  <div class="brand-name">KeyHarbor</div>
  <div class="band">
    <svg width="78" height="6" viewBox="0 0 78 6"><polygon points="0,3 78,0 78,6" fill="var(--accent-blue)"/></svg>
    <span class="tagline">Right Expertise, Exceptional Service</span>
    <svg width="78" height="6" viewBox="0 0 78 6"><polygon points="0,0 78,3 0,6" fill="var(--accent-green)"/></svg>
  </div>
</section>

<section class="card card--front">
  <div class="brand-square"></div>
  <div class="brand-name">KeyHarbor</div>

  <div class="details">
    <h1 class="person-name">Marissa Toll</h1>
    <p class="credentials">(BBus (Finance) LLB)<br>Licensed Conveyancer</p>
    <ul class="contact-list">
      <li>
        <svg viewBox="0 0 19 16"><path d="M2 5 Q9.5 0 17 5 L15 7 L12.5 6 L12.5 4.5 Q9.5 3.5 6.5 4.5 L6.5 6 L4 7 Z" fill="var(--accent-blue)"/><rect x="4.5" y="8" width="10" height="6" rx="1" fill="var(--accent-blue)"/></svg>
        <span>1300 682 917</span>
      </li>
      <li>
        <svg viewBox="0 0 19 16"><rect x="2" y="3" width="15" height="10" fill="var(--accent-green)"/><polyline points="2,3 9.5,9 17,3" fill="none" stroke="var(--card)" stroke-width="1.3"/></svg>
        <span>marissa@keyharbor.com.au</span>
      </li>
      <li>
        <svg viewBox="0 0 19 16"><path d="M7 2 L5.5 14 M12.5 2 L11 14 M3.5 6 H15.5 M3 10.5 H15" stroke="var(--sky)" stroke-width="1.8" fill="none"/></svg>
        <span>ABN: 48 913 706</span>
      </li>
    </ul>
    <p class="address">Suite 14, Level 3, 9 Calloway Road<br>Lindhurst Park, NSW 2178</p>
  </div>

  <div class="band">
    <svg width="78" height="6" viewBox="0 0 78 6"><polygon points="0,3 78,0 78,6" fill="var(--accent-blue)"/></svg>
    <span class="locations">Sydney&nbsp; | &nbsp;Melbourne&nbsp; | &nbsp;Brisbane</span>
    <svg width="78" height="6" viewBox="0 0 78 6"><polygon points="0,0 78,3 0,6" fill="var(--accent-green)"/></svg>
  </div>
</section>

</body>
</html>
```